Stationery Design Project - KTRV-PRIME

Presentation Folder
Size: A4
Notepad
Size: 250mm x 140mm
With Compliments Slip
Size: DL
210mm x 99mm
Letterhead
Size: A4 - 210mm x 297mm
Business Cards
Size: 90mm x 55mm

Company is called "KTRV-PRIME"
website: www.ktrvprime.com.au (under construction)

Offices: *Perth *Brisbane *Seoul *Hong Kong

If you need any further information please let me know!

Cheers

Neil

```html
<!DOCTYPE html>
<html lang="en">
<head>
<meta charset="utf-8">
<title>KTRV-PRIME Stationery Set</title>
<link href="https://fonts.googleapis.com/css2?family=Arimo:wght@400;700&display=swap" rel="stylesheet">
<style>
  :root {
    --backdrop: #4b4b4b;
    --paper: #ffffff;
    --brand-blue: #1d5ea8;
    --accent-blue: #2b8fd4;
    --band-blue: #1f4f9c;
    --ink: #3a3a3a;
    --ink-soft: #6b6b6b;
    --mark-grey: #8a8f96;
    --cube-light: #eef2f6;
    --cube-mid: #c9d6e3;
    --cube-blue: #6fb3e6;
  }
  * { box-sizing: border-box; margin: 0; padding: 0; }
  html, body { width: 1200px; height: 517px; overflow: hidden; }
  body {
    position: relative;
    background: var(--backdrop);
    font-family: "Arimo", Arial, sans-serif;
    color: var(--ink);
  }
  .sheet { position: absolute; background: var(--paper); overflow: hidden; }
  .band { position: absolute; left: 0; right: 0; bottom: 0; background: var(--band-blue); }

  .wordmark { position: absolute; display: flex; align-items: center; gap: 5px; }
  .wordmark .dot { width: 12px; height: 12px; background: var(--cube-mid); }
  .wordmark .name { font-weight: 400; color: var(--mark-grey); font-size: 12px; letter-spacing: .5px; }

  .cube-art {
    position: absolute;
    background: linear-gradient(150deg, var(--paper) 0%, var(--cube-light) 35%, var(--cube-mid) 70%, var(--cube-blue) 100%);
  }

  .tiny { font-size: 5.5px; line-height: 1.45; }
  .tiny p + p { margin-top: 4px; }
  .label { color: var(--accent-blue); font-weight: 700; text-transform: uppercase; font-size: 5.5px; }
  .heading-blue { color: var(--accent-blue); }

  /* letterhead */
  .letterhead { left: 33px; top: 33px; width: 285px; height: 455px; }
  .letterhead .band { height: 15px; }
  .letterhead .wordmark { left: 108px; top: 28px; }
  .lh-fields { position: absolute; left: 22px; top: 112px; width: 88px; }
  .lh-fields p { font-size: 5.5px; font-weight: 700; border-bottom: .5px solid #999; height: 11px; margin-bottom: 2px; }
  .lh-fields .gap { margin-top: 14px; }
  .lh-about { position: absolute; left: 110px; top: 110px; width: 158px; }
  .lh-about h3 { font-size: 7px; font-weight: 400; margin-bottom: 6px; }
  .lh-about p { margin-bottom: 6px; }
  .lh-office { position: absolute; left: 22px; top: 336px; width: 82px; }
  .lh-lower { position: absolute; left: 110px; top: 384px; width: 158px; }
  .lh-lower p + p { margin-top: 3px; }
  .lh-tagline { position: absolute; left: 22px; top: 410px; width: 82px; color: var(--ink-soft); }

  /* notepad */
  .notepad { left: 335px; top: 55px; width: 150px; height: 375px; }
  .notepad .wordmark { left: 40px; top: 24px; }
  .notepad .cube-art { right: 0; bottom: 0; width: 80px; height: 140px; }
  .np-office { position: absolute; left: 12px; top: 288px; width: 62px; line-height: 1.35; }
  .np-office p + p { margin-top: 3px; }

  /* compliments slip */
  .slip { left: 85px; top: 245px; width: 385px; height: 142px; }
  .slip .band { height: 7px; }
  .slip .wordmark { left: 14px; top: 14px; }
  .slip .wordmark .name { font-size: 14px; }
  .slip-tag { position: absolute; left: 150px; top: 14px; width: 90px; color: var(--ink-soft); }
  .slip-office { position: absolute; left: 24px; top: 56px; width: 90px; }
  .slip-compl { position: absolute; left: 118px; top: 56px; width: 110px; }
  .slip-compl h4 { font-size: 7px; font-weight: 400; margin-bottom: 4px; }
  .slip-compl .field { margin-bottom: 7px; }
  .slip-compl .check { margin: 0; }
  .tickbox { display: inline-block; width: 4px; height: 4px; border: .5px solid var(--ink); margin-right: 4px; vertical-align: middle; }
  .slip .cube-art { right: 0; top: 0; width: 140px; height: 135px; }

  /* folder */
  .folder { left: 520px; top: 27px; width: 650px; height: 480px; }
  .folder .band { height: 13px; bottom: 16px; }
  .folder-fold { position: absolute; left: 317px; top: 0; bottom: 29px; width: 1px; background: #dcdcdc; }
  .back-panel { position: absolute; left: 0; top: 0; width: 317px; height: 451px; overflow: hidden; }
  .back-panel .wordmark { left: 130px; top: 40px; }
  .back-tagline { position: absolute; left: 40px; top: 65px; width: 240px; text-align: center; font-size: 12.5px; line-height: 1.3; color: var(--accent-blue); }
  .back-panel .cube-art { left: 0; top: 240px; width: 317px; height: 140px; background: linear-gradient(180deg, var(--paper), var(--cube-light) 50%, var(--cube-mid)); }
  .offices { position: absolute; left: 95px; top: 357px; display: flex; gap: 10px; }
  .offices div { width: 67px; font-size: 5px; }
  .offices .label { font-size: 5px; }
  .front-panel { position: absolute; left: 318px; top: 0; width: 332px; height: 451px; }
  .front-panel .wordmark { left: 100px; top: 50px; }
  .front-panel .wordmark .dot { width: 22px; height: 22px; }
  .front-panel .wordmark .name { font-size: 16px; }
  .cities { position: absolute; left: 130px; top: 78px; font-size: 6.5px; line-height: 1.4; color: var(--mark-grey); }
  .front-panel .cube-art { left: 10px; top: 160px; width: 322px; height: 215px; background: linear-gradient(200deg, var(--cube-blue) 0%, var(--cube-mid) 35%, var(--cube-light) 75%, var(--paper)); }
  .photo-strip { position: absolute; left: 10px; top: 375px; width: 322px; height: 58px; display: flex; gap: 2px; }
  .photo-strip div { flex: 1; }
  .photo-mine { background: linear-gradient(180deg, #7aa0c4, #8a6a4a); }
  .photo-turbine { background: linear-gradient(180deg, #9fc4e6, #d9e6f2); }
  .photo-rig { background: linear-gradient(180deg, #c7d4e2, #5f7e9c); }
  .photo-tanker { background: linear-gradient(180deg, #2f6fa8, #16406a); }

  /* business cards */
  .card { position: absolute; width: 80px; height: 140px; border-radius: 8px; overflow: hidden; }
  .card-front { left: 755px; top: 160px; background: var(--paper); border: .5px solid #ccc; }
  .card-front .wordmark { left: 10px; top: 14px; }
  .card-front .wordmark .dot { width: 8px; height: 8px; }
  .card-front .wordmark .name { font-size: 8px; }
  .card-name { position: absolute; left: 8px; top: 48px; width: 66px; }
  .card-name strong { color: var(--brand-blue); font-size: 5.5px; display: block; }
  .card-details { position: absolute; left: 8px; top: 78px; width: 68px; font-size: 4.5px; line-height: 1.4; }
  .card-details p + p { margin-top: 3px; }
  .card-back { left: 880px; top: 170px; background: var(--brand-blue); color: #fff; }
  .card-back .web { position: absolute; left: 12px; top: 18px; font-size: 5px; }
  .card-back .cube-art { left: 0; top: 55px; width: 80px; height: 85px; background: linear-gradient(160deg, var(--brand-blue), var(--cube-blue) 60%, #d7e6f3); opacity: .9; }
  .card-back .spots { position: absolute; left: 10px; top: 60px; font-size: 4.5px; line-height: 3.2; color: #dcecfa; }
</style>
</head>
<body>

<section class="sheet letterhead">
  <div class="wordmark"><span class="dot"></span><span class="name">KTRV-PRIME</span></div>
  <div class="lh-fields">
    <p>TO:</p><p>Company:</p><p>Address:</p><p></p><p></p>
    <p class="gap">Tel:</p><p>Fax:</p><p>E-mail:</p>
  </div>
  <div class="lh-about tiny">
    <h3 class="heading-blue">About us</h3>
    <p>An independent specialised Health, Safety, Environment and Quality Recruitment Company was a vision of our company founder for many years until early 2008 that vision became a reality with the birth of ktrv prime. We are Australian privately owned and operated recruitment service company with offices in Perth Western Australia.</p>
    <p><span class="heading-blue">We operate exclusively in the Mining, Oil and Gas, Construction and Engineering sectors</span> and our clients range from engineering consultancies, major owner operator oil companies, international EPCMs to the largest diversified mining companies in the world.</p>
    <p>Inclusive to providing Health Safety, Environment and Quality professionals of all levels we also provide Risk Management, Emergency Response and Training personnel. These professionals are sourced locally and internationally to meet the unique requirements of our clients and candidates alike in today's dynamic and ever changing work place.</p>
    <p>Our primary approach is to provide unparalleled service to candidates and clients whilst never losing sight of what matters most, and we will always strive to do what is right by every person we place.</p>
  </div>
  <div class="lh-office tiny">
    <p class="label">Perth Office</p>
    <p>Suite 9, 212 Harlow Road<br>Subiaco<br>Western Australia 6008</p>
    <p>P | +61 (0) 8 6100 2210<br>F | +61 (0) 8 6100 2211<br>E | info@ktrvcorp.com.au<br>W | www.ktrvcorp.com.au</p>
  </div>
  <div class="lh-lower tiny">
    <p><strong>Engineering</strong> - Consultancies and service phases.</p>
    <p><strong>Construction</strong> - Local and International construction companies of all sizes.</p>
    <p>Our client base is diverse and consists of private and listed companies of all sizes. We at ktrv corp look forward to assisting you with your next career opportunity or recruitment requirements.</p>
  </div>
  <p class="lh-tagline tiny">Australia's number one group in health, safety, environmental and quality recruitment.</p>
  <div class="band"></div>
</section>

<section class="sheet notepad">
  <div class="wordmark"><span class="dot"></span><span class="name">KTRV-PRIME</span></div>
  <div class="cube-art" role="img" aria-label="Soft blue and white stacked block artwork"></div>
  <div class="np-office tiny">
    <p class="label">Perth Office</p>
    <p>Suite 9, 212 Harlow Road<br>P +61 (0) 8 6100 2210<br>F +61 (0) 8 6100 2211<br>info@ktrvcorp.com.au<br>www.ktrvcorp.com.au</p>
    <p>Australia's number one group in health, safety, environmental and quality recruitment.</p>
  </div>
</section>

<section class="sheet slip">
  <div class="wordmark"><span class="dot"></span><span class="name">KTRV-PRIME</span></div>
  <p class="slip-tag tiny">Australia's number one group in health, safety, environmental and quality recruitment.</p>
  <div class="slip-office tiny">
    <p class="label">Perth Office</p>
    <p>Suite 9, 212 Harlow Road<br>Subiaco<br>Western Australia 6008</p>
    <p>P | +61 (0) 8 6100 2210<br>F | +61 (0) 8 6100 2211<br>E | info@ktrvcorp.com.au<br>W | www.ktrvcorp.com.au</p>
  </div>
  <div class="slip-compl tiny">
    <h4 class="heading-blue">with compliments</h4>
    <p class="field">for:</p>
    <p class="field">date:</p>
    <p class="check"><span class="tickbox"></span>as agreed by telephone</p>
    <p class="check"><span class="tickbox"></span>as requested by you</p>
    <p class="check"><span class="tickbox"></span>for information only</p>
    <p class="check"><span class="tickbox"></span>please phone / fax</p>
  </div>
  <div class="cube-art" role="img" aria-label="Soft blue and white stacked block artwork"></div>
  <div class="band"></div>
</section>

<section class="sheet folder">
  <div class="back-panel">
    <div class="wordmark"><span class="dot"></span><span class="name">KTRV-PRIME</span></div>
    <p class="back-tagline">Australia's number one group in health, safety, environmental and quality recruitment.</p>
    <div class="cube-art" role="img" aria-label="Pale grey stacked block artwork"></div>
    <div class="offices tiny">
      <div>
        <p class="label">Brisbane Office</p>
        <p>Level 14, Riverside Tower<br>120 Mary Street<br>Queensland 4000</p>
        <p>P | +61 (0) 7 3000 4410<br>F | +61 (0) 7 3000 4411<br>E | info@ktrvcorp.com.au</p>
      </div>
      <div>
        <p class="label">Seoul Office</p>
        <p>Level 18, Hanbit Tower<br>220 Teheran-ro<br>Yeoksam-dong, Gangnam-Gu<br>Seoul, Republic of Korea</p>
        <p>P | +82 (0) 2 5550 1180<br>F | +82 (0) 2 5550 1181<br>E | seoul@ktrvcorp.com.au</p>
      </div>
      <div>
        <p class="label">Perth Office</p>
        <p>Suite 9, 212 Harlow Road<br>Subiaco<br>Western Australia 6008</p>
        <p>P | +61 (0) 8 6100 2210<br>F | +61 (0) 8 6100 2211<br>E | info@ktrvcorp.com.au</p>
      </div>
    </div>
  </div>
  <div class="folder-fold"></div>
  <div class="front-panel">
    <div class="wordmark"><span class="dot"></span><span class="name">KTRV-PRIME</span></div>
    <p class="cities">Perth<br>Brisbane<br>Seoul<br>Hong Kong</p>
    <div class="cube-art" role="img" aria-label="Large blue and white stacked block artwork"></div>
    <div class="photo-strip">
      <div class="photo-mine" role="img" aria-label="Photo of a mining excavator at an open pit"></div>
      <div class="photo-turbine" role="img" aria-label="Photo of wind turbines against the sky"></div>
      <div class="photo-rig" role="img" aria-label="Photo of an offshore oil platform"></div>
      <div class="photo-tanker" role="img" aria-label="Photo of a gas tanker ship at sea"></div>
    </div>
  </div>
  <div class="band"></div>
</section>

<section class="card card-front">
  <div class="wordmark"><span class="dot"></span><span class="name">KTRV-PRIME</span></div>
  <div class="card-name tiny">
    <strong>Mr. Name W. SURNAME</strong>
    <span>(position/department)</span>
  </div>
  <div class="card-details">
    <p>Perth Suite 9, 212 Harlow Road<br>Office Subiaco WA 6008</p>
    <p>P +61 (0) 8 6100 2210<br>F +61 (0) 8 6100 2211<br>E info@ktrvcorp.com.au</p>
  </div>
</section>

<section class="card card-back">
  <p class="web">www.ktrvprime.com.au</p>
  <div class="cube-art" role="img" aria-label="Blue stacked block artwork"></div>
  <p class="spots">Perth Office<br>Hong Kong Office<br>Brisbane Office<br>Seoul Office</p>
</section>

</body>
</html>
```